Copper Lark Treks Flyer

I have an adventure travel company and I need a flyer to promote my trip to Ukraine.
I would like to have a universal flyer that I can change based on the trip.
The Title should say "Travel to Ukraine: 9 Day Eastern European Adventure"
The date should be under the title.
The background photo should be kiev2.jpg
The highlights of the trip, then price $1200 and what it includes. See the text for highlights and includes sections here:
http://www.copperlarktreks.com/#!featured-trip
The website link (www.copperlarktreks.com) should be somewhere in the bottom.
You can use other photos provided or from my website that relates to Ukraine trip.

```html
<!DOCTYPE html>
<html lang="en">
<head>
<meta charset="utf-8">
<title>Copper Lark Treks – Travel to Ukraine</title>
<link rel="stylesheet" href="https://fonts.googleapis.com/css2?family=Fredoka:wght@600&family=Arimo:wght@400;700&display=swap">
<style>
  :root {
    --frame-green: #7cc23a;
    --frame-green-dark: #4f9a25;
    --paper: #ffffff;
    --ink: #1a1a1a;
    --white: #ffffff;
    --bullet: #6bbf3a;
    --burst: #f08a1c;
    --burst-edge: #c9650a;
    --meadow-top: #2f8d1c;
    --meadow-mid: #7fcf44;
    --meadow-light: #c6eb8e;
  }
  * { box-sizing: border-box; margin: 0; padding: 0; }
  html, body { width: 861px; height: 1200px; overflow: hidden; background: var(--paper); }
  .flyer {
    position: relative; width: 861px; height: 1200px; overflow: hidden;
    background: var(--paper);
    font-family: "Arimo", Arial, sans-serif;
  }
  .frame-strip {
    position: absolute; top: 0; bottom: 0; width: 43px;
    background: linear-gradient(180deg, var(--frame-green) 0%, var(--frame-green-dark) 100%);
  }
  .frame-strip--left { left: 0; }
  .frame-strip--right { right: 0; }

  .hero-photo {
    position: absolute; left: 43px; right: 42px; top: 0; height: 720px;
    background: linear-gradient(180deg,
      #1c47b5 0%, #3f74cf 12%, #9fc0e6 20%, #e9f0f6 26%, #8fb0c9 30%,
      #1e5786 32%, #2f6f96 40%, #3d7a6a 46%, #4b7a32 54%, #3f6e25 70%, #557f30 100%);
    clip-path: polygon(0 0, 100% 0, 100% 100%, 0 100%, 0 46%, 4% 44%, 3% 40%, 5% 37%, 0 35%);
  }

  .title {
    position: absolute; left: 0; width: 861px; top: 14px; text-align: center;
    font-family: "Fredoka", "Arial Rounded MT Bold", sans-serif; font-weight: 600;
    font-size: 86px; letter-spacing: 3px; line-height: 1; color: var(--white);
    -webkit-text-stroke: 2px #222;
    text-shadow: 3px 4px 0 #333;
  }
  .subtitle {
    position: absolute; left: 0; width: 861px; top: 110px; text-align: center;
    font-size: 31px; color: var(--white); letter-spacing: 0.5px;
  }
  .dates {
    position: absolute; left: 0; width: 790px; top: 157px; text-align: center;
    font-weight: 700; font-size: 18px; color: var(--ink);
  }
  .tour-lines {
    position: absolute; left: 0; width: 790px; top: 192px; text-align: center;
    font-weight: 700; font-size: 21px; line-height: 26px; color: var(--ink);
  }
  .booking {
    position: absolute; left: 0; width: 790px; top: 304px; text-align: center;
    font-weight: 700; font-size: 18px; line-height: 26px; color: var(--white);
    letter-spacing: 0.5px;
  }
  .price-burst { position: absolute; left: 676px; top: 140px; width: 152px; height: 152px; }

  .snapshot {
    position: absolute; background: var(--paper); padding: 7px;
    box-shadow: 3px 4px 8px rgba(0,0,0,0.45);
  }
  .snapshot__image { width: 100%; height: 100%; }
  .snapshot--lavra { left: 80px; top: 574px; width: 234px; height: 178px; transform: rotate(-4deg); }
  .snapshot--lavra .snapshot__image { background: linear-gradient(180deg, #8fa7b8 0%, #c9b25a 45%, #7a6c52 75%, #5f6f45 100%); }
  .snapshot--tram { left: 330px; top: 560px; width: 212px; height: 200px; transform: rotate(3deg); }
  .snapshot--tram .snapshot__image { background: linear-gradient(180deg, #c8cbc4 0%, #9aa08a 40%, #b3403a 60%, #6f6a60 100%); }
  .snapshot--cliff { left: 540px; top: 566px; width: 240px; height: 190px; transform: rotate(9deg); }
  .snapshot--cliff .snapshot__image { background: linear-gradient(160deg, #a9b9c6 0%, #7f93a0 45%, #55633e 75%, #8a8b82 100%); }

  .meadow {
    position: absolute; left: 80px; right: 42px; top: 640px; height: 520px;
    background: linear-gradient(180deg, var(--meadow-top) 0%, var(--meadow-mid) 18%, var(--meadow-light) 55%, var(--meadow-mid) 88%, var(--meadow-top) 100%);
    clip-path: polygon(0 6%, 100% 0, 100% 97%, 92% 100%, 84% 96%, 72% 99%, 60% 96%, 48% 99%, 36% 96%, 24% 100%, 12% 96%, 4% 99%, 0 97%);
  }
  .highlights {
    position: absolute; left: 89px; top: 780px; width: 710px; color: var(--ink);
  }
  .highlights__heading { font-weight: 700; font-size: 18px; letter-spacing: 0.5px; margin-bottom: 7px; margin-left: 12px; }
  .highlights__list { list-style: none; font-size: 18px; line-height: 25px; }
  .highlights__item { position: relative; padding-left: 12px; margin-bottom: 3px; }
  .highlights__item::before {
    content: ""; position: absolute; left: -2px; top: 8px; width: 11px; height: 11px;
    border-radius: 50%; background: var(--bullet);
  }
  .website {
    position: absolute; left: 0; width: 861px; top: 1091px; text-align: center;
    font-weight: 700; font-size: 19px; color: var(--ink);
  }
</style>
</head>
<body>
<div class="flyer">
  <div class="frame-strip frame-strip--left"></div>
  <div class="frame-strip frame-strip--right"></div>

  <div class="hero-photo" role="img" aria-label="Photo of the Crimean coast: blue sky, the Black Sea and a green hillside town with a rocky cliff"></div>

  <h1 class="title">Travel to Ukraine</h1>
  <p class="subtitle">9 Day Eastern European Adventure</p>
  <p class="dates">Fri May 18 - &nbsp;Sun May 27</p>
  <p class="tour-lines">Historic Kiev, Exclusive Crimea<br>Hiking and Caves tour,<br>Black Sea, Odessa and its Catacombs</p>
  <p class="booking">Deposit: $200.00 to reserve your spot<br>Sale ends: &nbsp;April 20th , 2012</p>

  <svg class="price-burst" viewBox="0 0 152 152" aria-label="Price $1200">
    <polygon fill="var(--burst)" stroke="var(--burst-edge)" stroke-width="2"
      points="76,2 85,20 101,6 104,26 123,18 119,38 140,37 129,54 149,61 133,74 149,88 130,95 140,113 119,113 122,134 103,126 99,146 84,133 76,150 66,133 53,146 49,126 30,134 33,113 12,113 22,95 3,88 19,74 3,61 23,54 12,37 33,38 29,18 48,26 51,6 67,20"/>
    <g transform="rotate(-16 76 76)" fill="var(--white)" font-family="Arimo, Arial, sans-serif" font-weight="700" text-anchor="middle">
      <text x="80" y="70" font-size="27" letter-spacing="1">Price</text>
      <text x="76" y="102" font-size="29" letter-spacing="1">$1200</text>
    </g>
  </svg>

  <div class="meadow"></div>

  <figure class="snapshot snapshot--lavra"><div class="snapshot__image" role="img" aria-label="Photo of golden church domes above the Dnieper river in Kiev"></div></figure>
  <figure class="snapshot snapshot--tram"><div class="snapshot__image" role="img" aria-label="Photo of a red tram on a tree-lined street in Odessa"></div></figure>
  <figure class="snapshot snapshot--cliff"><div class="snapshot__image" role="img" aria-label="Photo of a pine tree on a rocky Crimean mountain ledge"></div></figure>

  <section class="highlights">
    <h2 class="highlights__heading">HIGHLIGHTS:</h2>
    <ul class="highlights__list">
      <li class="highlights__item">Discover Kiev- the birthplace of Eastern Slavic Civilization</li>
      <li class="highlights__item">Meet Crimea's fascinating Tatar Minority in Bakhchysaray -<br>former capital of Crimean Tatar Khans</li>
      <li class="highlights__item">Walk to Chufut-Kale - Crimea's best preserved &nbsp;medieval cave town</li>
      <li class="highlights__item">Hike in the most spectacular areas in Karabi and explore the caves<br>with a group of professional speleologist</li>
      <li class="highlights__item">Inhale the magic Yalta's air- an invigorating blend of sea and pine<br>forest sprinkled with mountain chill</li>
      <li class="highlights__item">Visit Odessa- "the Pearl by the Black Sea", Catacombs, Opera<br>house, the factory of sparkling wines and famous Potemkin Steps</li>
    </ul>
  </section>

  <p class="website">www.copperlarktreks.com</p>
</div>
</body>
</html>
```